Psychiatric Office Needs a Website- 1st Time Ever!

Been in practice since 2003 with no website, but finally ready to dive in. We are Maplecrest Behavioral Healthcare, a mental health outpatient practice based in Fayetteville, Georgia that sees diverse individuals and families from childhood to advanced age for a variety of conditions. We've grown by word of mouth and referral but would now like to have a digital footprint. Be the pioneer of our website and we will be sure to share. We would like to see designs that are modern, animated, fairly colorful, easy to read, and caters to all ages. Also, we would like the design to take the whole page (not be centered) and can be viewed well on phone/tablet. Please see our outline for more information. Our motto/slogan is: Maplecrest Behavioral Healthcare- A step forward in your wellness journey, so the design should try to reflect that.
Updates

Target Market(s)

Children through elderly

Industry/Entity Type

Medical

Logo Text

Stepping forward in your wellness journey

Number of Pages Required

1 page

Colors

Designer to choose colors to be used in the design.

Requirements
Must have
• Animation or moving pictures.
• Color.
• Concise.
• User friendly
• Diversity in the stock photos

```html
<!DOCTYPE html>
<html lang="en">
<head>
<meta charset="utf-8">
<title>Maplecrest Behavioral Healthcare</title>
<link href="https://fonts.googleapis.com/css2?family=Open+Sans:ital,wght@0,400;0,600;0,700;1,400&family=Source+Sans+3:wght@400;600&display=swap" rel="stylesheet">
<style>
:root{
  --blue:#2a9bd6;
  --blue-dark:#1f86c0;
  --green:#6cb33f;
  --green-dark:#5a9e30;
  --ink:#333;
  --muted:#555;
  --topbar:#2f2f2f;
  --white:#fff;
  --line:#dcdcdc;
}
*{margin:0;padding:0;box-sizing:border-box}
html,body{width:1200px;height:3462px;overflow:hidden}
body{position:relative;font-family:"Open Sans",Arial,sans-serif;color:var(--ink);background:var(--white)}
.abs{position:absolute}
.heading{font-family:"Source Sans 3","Open Sans",sans-serif;font-weight:400}

/* header */
.topbar{left:0;top:0;width:1200px;height:58px;background:var(--topbar)}
.topbar .item{top:16px;font-size:14px;color:#eee;display:flex;align-items:center;gap:8px}
.topbar .ico{width:18px;height:18px}
.portal-btn{left:935px;top:7px;width:177px;height:44px;border-radius:22px;background:var(--blue);color:var(--white);font-weight:700;font-size:19px;display:flex;align-items:center;justify-content:center}
.navbar{left:0;top:58px;width:1200px;height:74px;background:var(--green)}
.nav-link{top:86px;font-size:17px;color:var(--white)}
.nav-home{left:358px;top:50px;width:104px;height:82px;background:var(--blue);color:var(--white);font-size:17px;display:flex;align-items:flex-end;justify-content:center;padding-bottom:28px}
.brand{left:80px;top:22px;width:110px;height:110px;border-radius:50%;background:var(--blue);border:5px solid var(--white);display:flex;align-items:center;justify-content:center;text-align:center;color:var(--white);font-size:13px;font-weight:600;line-height:1.2;padding:10px}

/* hero */
.hero{left:0;top:132px;width:1200px;height:572px;background:linear-gradient(135deg,#c9d9a6 0%,#e6dccb 35%,#b9c7a0 65%,#7e9a55 100%)}
.hero-box{left:208px;top:316px;width:784px;height:173px;background:rgba(40,40,40,.55)}
.hero-title{left:208px;top:318px;width:784px;text-align:center;font-size:46px;color:var(--white)}
.hero-tag{left:208px;top:372px;width:784px;text-align:center;font-size:19px;font-style:italic;color:#f0f0f0}
.hero-btn{left:508px;top:415px;width:184px;height:53px;background:var(--blue);color:var(--white);font-size:19px;display:flex;align-items:center;justify-content:center}
.slide-arrow{width:46px;height:56px;background:rgba(255,255,255,.75);display:flex;align-items:center;justify-content:center}

/* vision & mission */
.vm-left{left:0;top:704px;width:600px;height:365px;background:var(--blue)}
.vm-right{left:600px;top:704px;width:600px;height:365px;background:var(--green)}
.vm-title{top:748px;display:flex;align-items:center;gap:14px;color:var(--white);font-size:36px}
.vm-rule{top:800px;width:160px;height:2px;background:var(--white)}
.vm-text{top:820px;width:372px;font-size:14.5px;line-height:24.5px;color:var(--white)}
.vm-badge{left:462px;top:738px;width:276px;height:276px;border-radius:50%;background:var(--white);display:flex;align-items:center;justify-content:center}
.vm-badge span{width:244px;height:244px;border-radius:50%;background:var(--blue);color:var(--white);font-size:24px;font-weight:600;line-height:1.3;display:flex;align-items:center;justify-content:center;text-align:center;padding:30px}

/* services */
.services{left:0;top:1069px;width:1200px;height:831px;background:radial-gradient(ellipse at 70% 40%,#dde3e8 0%,#eceff1 45%,#f6f6f6 100%)}
.services-title{left:0;top:1112px;width:1200px;text-align:center;font-size:38px;color:var(--white);text-shadow:0 1px 3px rgba(0,0,0,.25)}
.svc{width:300px;font-size:14px;line-height:21px;color:var(--ink)}
.svc h3{font-weight:400;font-size:17px;color:var(--blue);margin-bottom:1px}
.svc a{color:var(--ink);font-weight:700;text-decoration:underline}

/* conditions */
.conditions{left:0;top:1900px;width:1200px;height:553px;background:linear-gradient(90deg,#2a8fd0 0%,#3ba0b8 50%,#6cb33f 100%)}
.cond-title{left:0;top:1958px;width:1200px;text-align:center;font-size:36px;color:var(--white)}
.cond-rule{left:400px;top:2010px;width:400px;height:1px;background:rgba(255,255,255,.6)}
.cond-card{top:2052px;width:252px}
.cond-photo{width:252px;height:166px;box-shadow:3px 4px 6px rgba(0,0,0,.35)}
.cond-name{margin-top:22px;text-align:center;font-size:19px;line-height:22px;color:var(--white);height:44px;display:flex;align-items:center;justify-content:center}
.cond-text{margin-top:6px;text-align:center;font-size:13px;line-height:19px;color:var(--white)}
.cond-arrow{top:2114px;width:32px;height:32px;background:var(--white);display:flex;align-items:center;justify-content:center}
.dots{left:572px;top:2418px;display:flex;gap:6px}
.dots i{width:14px;height:14px;border:1px solid var(--white)}
.dots i.on{background:var(--white)}

/* faq & news */
.split{left:610px;top:2453px;width:6px;height:432px;background:linear-gradient(90deg,#eee,#fff)}
.sec-title{top:2500px;font-size:38px;color:var(--blue)}
.faq{left:76px;top:2558px;width:520px;border:1px solid var(--line)}
.faq-q{height:44px;display:flex;align-items:center;gap:14px;padding-left:14px;font-size:19px;color:var(--blue);border-top:1px solid var(--line)}
.faq-q:first-child{border-top:none}
.faq-q .sign{width:22px;height:22px;display:flex;align-items:center;justify-content:center}
.faq-a{padding:6px 20px 14px 20px;font-size:12.5px;line-height:19px;color:var(--muted);border-top:1px solid var(--line)}
.news{left:667px;width:460px;height:114px}
.news-photo{left:0;top:0;width:115px;height:114px}
.news h4{position:absolute;left:131px;top:6px;font-weight:400;font-size:17px;color:var(--blue)}
.news .date{position:absolute;left:131px;top:33px;font-size:11px;color:var(--green)}
.news p{position:absolute;left:131px;top:50px;width:300px;font-size:13.5px;line-height:21px;color:var(--ink)}
.news .more{position:absolute;left:131px;top:98px;font-size:12px;color:var(--blue)}
.news-rule{left:667px;top:2691px;width:455px;height:1px;background:var(--line)}

/* cta band */
.band{left:0;top:2885px;width:1200px;height:132px;background:var(--blue)}
.band p{position:absolute;left:81px;top:32px;width:790px;font-size:14.5px;line-height:29px;color:var(--white)}
.band-btn{left:895px;top:2908px;width:229px;height:55px;background:var(--green);color:var(--white);font-size:18px;display:flex;align-items:center;justify-content:center}

/* footer */
.footer{left:0;top:3017px;width:1200px;height:387px;background:linear-gradient(120deg,#4d6b3a 0%,#6a8550 40%,#5c7d46 70%,#3e5e33 100%)}
.foot-title{top:3042px;font-size:20px;color:var(--white);letter-spacing:.5px}
.field{left:81px;width:445px;background:var(--white);font-size:13px;color:#666;padding:8px 12px}
.submit{left:81px;top:3332px;width:184px;height:54px;background:var(--blue);color:var(--white);font-size:18px;display:flex;align-items:center;justify-content:center}
.foot-list{left:570px;top:3083px;list-style:none}
.foot-list li{font-size:14px;line-height:28.5px;color:var(--white);display:flex;align-items:center;gap:12px}
.foot-list li::before{content:"";width:7px;height:7px;border-radius:50%;background:var(--blue)}
.find{left:872px;display:flex;gap:16px;font-size:14px;line-height:24px;color:var(--white)}
.find svg{flex:none;margin-top:2px}
.social{top:3316px;width:48px;height:48px;border-radius:50%;background:var(--blue)}
.copy{left:0;top:3404px;width:1200px;height:58px;background:#3b5a2e;border-top:1px solid rgba(255,255,255,.3);display:flex;align-items:center;justify-content:center;font-size:13px;color:var(--white)}
.copy b{font-weight:700;margin-right:4px}
</style>
</head>
<body>

<!-- header -->
<div class="abs topbar"></div>
<div class="abs topbar">
  <div class="abs item" style="left:300px">
    <svg class="ico" viewBox="0 0 20 20"><circle cx="10" cy="10" r="8" fill="none" stroke="#6cb33f" stroke-width="2"/><path d="M10 5v5l3 2" stroke="#6cb33f" stroke-width="2" fill="none"/></svg>
    Monday - Friday : 10.00 A.M to 8.00 P.M
  </div>
  <div class="abs item" style="left:618px">
    <svg class="ico" viewBox="0 0 20 20"><rect x="2" y="2" width="16" height="16" rx="3" fill="none" stroke="#6cb33f" stroke-width="2"/><path d="M7 6l2 2-1 2 2 2 2-1 2 2-2 2c-4 0-8-4-8-8z" fill="#6cb33f"/></svg>
    +1-555-014-2290
  </div>
  <div class="abs item" style="left:785px">LOGIN</div>
  <div class="abs item" style="left:840px">
    <svg class="ico" viewBox="0 0 20 20"><circle cx="10" cy="6" r="4" fill="#6cb33f"/><path d="M3 19c0-5 3-8 7-8s7 3 7 8z" fill="#6cb33f"/></svg>
    Patient
  </div>
  <div class="abs portal-btn">Patient Portal</div>
</div>
<div class="abs navbar"></div>
<div class="abs nav-home">Home</div>
<div class="abs nav-link" style="left:503px">About Us</div>
<div class="abs nav-link" style="left:605px">Services</div>
<div class="abs nav-link" style="left:700px">Conditions We Treat</div>
<div class="abs nav-link" style="left:888px">New Patients</div>
<div class="abs nav-link" style="left:1020px">Contact Us</div>
<div class="abs brand">Maplecrest Behavioral Healthcare</div>

<!-- hero -->
<div class="abs hero" role="img" aria-label="Photo of a smiling multi-generation family with grandparents, parents and children outdoors in a sunny park"></div>
<div class="abs hero-box"></div>
<h1 class="abs heading hero-title">Maplecrest Behavioral Healthcare</h1>
<div class="abs hero-tag">A step forward in your wellness journey</div>
<div class="abs hero-btn">CONTACT US</div>
<div class="abs slide-arrow" style="left:42px;top:376px"><svg width="14" height="24" viewBox="0 0 14 24"><path d="M12 2L2 12l10 10" stroke="#555" stroke-width="2" fill="none"/></svg></div>
<div class="abs slide-arrow" style="left:1112px;top:376px"><svg width="14" height="24" viewBox="0 0 14 24"><path d="M2 2l10 10L2 22" stroke="#555" stroke-width="2" fill="none"/></svg></div>

<!-- vision & mission -->
<div class="abs vm-left"></div>
<div class="abs vm-right"></div>
<div class="abs vm-title heading" style="left:81px">
  <svg width="30" height="40" viewBox="0 0 30 40"><path d="M4 22l18-16 4 4-16 18z" fill="#fff"/><path d="M12 26l-6 12M14 26l6 12" stroke="#fff" stroke-width="2.5"/></svg>
  VISION
</div>
<div class="abs vm-rule" style="left:81px"></div>
<p class="abs vm-text" style="left:78px">Lorem Ipsum is simply dummy text of the printing and typesetting industry. Lorem Ipsum has been the industry's standard dummy text ever since the 1500s, when an unknown printer took a galley of type and scrambled it to make a type specimen book. It has survived not only five centuries, but also the leap into electronic typesetting, remaining essentially unchanged.</p>
<div class="abs vm-title heading" style="left:768px">
  <svg width="34" height="34" viewBox="0 0 34 34"><circle cx="16" cy="18" r="13" fill="none" stroke="#fff" stroke-width="3"/><circle cx="16" cy="18" r="6" fill="none" stroke="#fff" stroke-width="3"/><path d="M16 18L31 3" stroke="#fff" stroke-width="3"/></svg>
  MISSION
</div>
<div class="abs vm-rule" style="left:768px"></div>
<p class="abs vm-text" style="left:768px">Lorem Ipsum is simply dummy text of the printing and typesetting industry. Lorem Ipsum has been the industry's standard dummy text ever since the 1500s, when an unknown printer took a galley of type and scrambled it to make a type specimen book. It has survived not only five centuries, but also the leap into electronic typesetting, remaining essentially unchanged.</p>
<div class="abs vm-badge"><span>Maplecrest Behavioral Healthcare</span></div>

<!-- services -->
<div class="abs services" role="img" aria-label="Soft blurred photo of a clinician talking with a patient in a bright office"></div>
<h2 class="abs heading services-title">SERVICES</h2>
<svg class="abs" style="left:0;top:0" width="1200" height="1900" viewBox="0 0 1200 1900">
  <g stroke="#9ccb6a" stroke-width="2">
    <line x1="600" y1="1401" x2="565" y2="1269"/>
    <line x1="600" y1="1401" x2="688" y2="1258"/>
    <line x1="600" y1="1401" x2="803" y2="1412"/>
    <line x1="600" y1="1401" x2="392" y2="1424"/>
    <line x1="600" y1="1401" x2="445" y2="1597"/>
    <line x1="600" y1="1401" x2="768" y2="1592"/>
    <line x1="600" y1="1401" x2="607" y2="1662"/>
  </g>
  <circle cx="600" cy="1401" r="94" fill="#fff" stroke="#2a9bd6" stroke-width="3"/>
  <circle cx="600" cy="1401" r="70" fill="#e8f4fb"/>
  <g fill="#fff" stroke="#2a9bd6" stroke-width="2">
    <circle cx="578" cy="1312" r="6"/><circle cx="655" cy="1323" r="6"/><circle cx="693" cy="1406" r="6"/>
    <circle cx="507" cy="1411" r="6"/><circle cx="540" cy="1474" r="6"/><circle cx="662" cy="1471" r="6"/><circle cx="601" cy="1495" r="6"/>
  </g>
  <g stroke="#2a9bd6" stroke-width="6">
    <circle cx="565" cy="1269" r="60" fill="#d9b9a8"/>
    <circle cx="688" cy="1258" r="60" fill="#c9a07e"/>
    <circle cx="803" cy="1412" r="60" fill="#8fb5cf"/>
    <circle cx="392" cy="1424" r="60" fill="#c8b49a"/>
    <circle cx="445" cy="1597" r="60" fill="#a9a49c"/>
    <circle cx="768" cy="1592" r="60" fill="#c7a47d"/>
    <circle cx="607" cy="1662" r="60" fill="#7f6d5e"/>
  </g>
</svg>
<div class="abs svc" style="left:138px;top:1226px"><h3>Diagnostic evaluation and treatment</h3>Lorem Ipsum is simply dummy text of the printing and text typesetting industry.<a>READ MORE</a></div>
<div class="abs svc" style="left:768px;top:1207px"><h3>Transcranial Magnetic Stimulation</h3>Lorem Ipsum is simply dummy text of the printing and text typesetting industry.<a>READ MORE</a></div>
<div class="abs svc" style="left:81px;top:1392px"><h3>Psychopharmacology</h3>Lorem Ipsum is simply dummy text of the printing and text typesetting industry.<a>READ MORE</a></div>
<div class="abs svc" style="left:886px;top:1366px"><h3>Groups</h3>Lorem Ipsum is simply dummy text of the printing and text typesetting industry.<a>READ MORE</a></div>
<div class="abs svc" style="left:99px;top:1580px"><h3>Bariatric pre-surgical consultation</h3>Lorem Ipsum is simply dummy text of the printing and text typesetting industry.<a>READ MORE</a></div>
<div class="abs svc" style="left:861px;top:1553px"><h3>Autism Center</h3>Lorem Ipsum is simply dummy text of the printing and text typesetting industry.<a>READ MORE</a></div>
<div class="abs svc" style="left:501px;top:1756px;width:220px"><h3>Developmental disabilities</h3>Lorem Ipsum is simply dummy text of the printing and text typesetting industry.<a>READ MORE</a></div>

<!-- conditions -->
<div class="abs conditions"></div>
<h2 class="abs heading cond-title">CONDITIOND WE TREAT</h2>
<div class="abs cond-rule"></div>
<div class="abs cond-arrow" style="left:32px"><svg width="10" height="16" viewBox="0 0 10 16"><path d="M8 2L2 8l6 6" stroke="#2a9bd6" stroke-width="2" fill="none"/></svg></div>
<div class="abs cond-arrow" style="left:1138px"><svg width="10" height="16" viewBox="0 0 10 16"><path d="M2 2l6 6-6 6" stroke="#6cb33f" stroke-width="2" fill="none"/></svg></div>
<div class="abs cond-card" style="left:76px">
  <div class="cond-photo" role="img" aria-label="Photo of a stressed woman holding her head" style="background:linear-gradient(135deg,#3a302a,#8a6a55)"></div>
  <div class="cond-name">Mood Disorders</div>
  <p class="cond-text">Lorem Ipsum is simply dummy text of the printing and typesetting industry. Lorem Ipsum has been the industry's standard dummy text ever since.</p>
</div>
<div class="abs cond-card" style="left:344px">
  <div class="cond-photo" role="img" aria-label="Photo of a caregiver comforting a woman on a sofa" style="background:linear-gradient(135deg,#e5e9ee,#6a8fb5)"></div>
  <div class="cond-name">Anxiety Disorders</div>
  <p class="cond-text">Lorem Ipsum is simply dummy text of the printing and typesetting industry. Lorem Ipsum has been the industry's standard dummy text ever since.</p>
</div>
<div class="abs cond-card" style="left:609px">
  <div class="cond-photo" role="img" aria-label="Photo of a therapist in session with a client in a library office" style="background:linear-gradient(135deg,#8a6b52,#c8b8a2)"></div>
  <div class="cond-name">Psychotic Disorders</div>
  <p class="cond-text">Lorem Ipsum is simply dummy text of the printing and typesetting industry. Lorem Ipsum has been the industry's standard dummy text ever since.</p>
</div>
<div class="abs cond-card" style="left:872px">
  <div class="cond-photo" role="img" aria-label="Photo of a smiling mother hugging her young daughter" style="background:linear-gradient(135deg,#9a6a45,#d8b48d)"></div>
  <div class="cond-name">Common Disorders<br>of Childhood</div>
  <p class="cond-text">Lorem Ipsum is simply dummy text of the printing and typesetting industry. Lorem Ipsum has been the industry's standard dummy text ever since.</p>
</div>
<div class="abs dots"><i></i><i class="on"></i><i></i></div>

<!-- faq & news -->
<div class="abs split"></div>
<h2 class="abs heading sec-title" style="left:81px">FAQ</h2>
<div class="abs faq">
  <div class="faq-q"><span class="sign" style="background:var(--blue)"><svg width="12" height="12"><rect y="5" width="12" height="2.5" fill="#fff"/></svg></span>What do I need to bring with me to my first visit?</div>
  <p class="faq-a">Lorem Ipsum is simply dummy text of the printing and typesetting industry. Lorem Ipsum has been the industry's standard dummy text ever since the 1500s,It has survived not only five centuries, but also the leap into electronic typesetting, remaining essentially unchanged.</p>
  <div class="faq-q"><span class="sign"><svg width="16" height="16"><rect y="6.5" width="16" height="3" fill="#6cb33f"/><rect x="6.5" width="3" height="16" fill="#6cb33f"/></svg></span>How long do I have to wait to be seen?</div>
  <div class="faq-q"><span class="sign"><svg width="16" height="16"><rect y="6.5" width="16" height="3" fill="#6cb33f"/><rect x="6.5" width="3" height="16" fill="#6cb33f"/></svg></span>Why is my child not doing well in school?</div>
  <div class="faq-q"><span class="sign"><svg width="16" height="16"><rect y="6.5" width="16" height="3" fill="#6cb33f"/><rect x="6.5" width="3" height="16" fill="#6cb33f"/></svg></span>What typs of insurance do you accept?</div>
</div>
<h2 class="abs heading sec-title" style="left:667px">LATEST NEWS</h2>
<div class="abs news" style="top:2558px">
  <div class="abs news-photo" role="img" aria-label="Photo of a young girl looking thoughtful" style="background:linear-gradient(135deg,#6b8fb8,#c9a58a)"></div>
  <h4>Lorem Ipsum is simply dummy text</h4>
  <span class="date">&#9632; 10 JULY 2016</span>
  <p>Lorem Ipsum is simply dummy text of the printing and typesetting industry.....</p>
  <span class="more">READ MORE &nbsp;&nbsp;&raquo;</span>
</div>
<div class="abs news-rule"></div>
<div class="abs news" style="top:2717px">
  <div class="abs news-photo" role="img" aria-label="Photo of a family reading together at home" style="background:linear-gradient(135deg,#b88a60,#e3cfb2)"></div>
  <h4>Lorem Ipsum is simply dummy text</h4>
  <span class="date">&#9632; 10 JULY 2016</span>
  <p>Lorem Ipsum is simply dummy text of the printing and typesetting industry.....</p>
  <span class="more">READ MORE &nbsp;&nbsp;&raquo;</span>
</div>

<!-- cta band -->
<div class="abs band"><p>Lorem Ipsum is simply dummy text of the printing and typesetting industry. Lorem Ipsum has been the industry's standard dummy text ever since the 1500s, when an unknown printer took a galley of type and scrambled.</p></div>
<div class="abs band-btn">NEW PATIENT FORM</div>

<!-- footer -->
<div class="abs footer" role="img" aria-label="Blurred green-toned photo of smiling children outdoors"></div>
<div class="abs foot-title" style="left:81px">QUICK INQUIRY</div>
<div class="abs field" style="top:3076px;height:46px;padding-top:14px">Name*</div>
<div class="abs field" style="top:3132px;height:42px;padding-top:12px">Email*</div>
<div class="abs field" style="top:3184px;height:42px;padding-top:12px">Services*</div>
<div class="abs field" style="top:3236px;height:83px">Message*</div>
<div class="abs submit">SUBMIT</div>
<div class="abs foot-title" style="left:570px">OUR SERVICES</div>
<ul class="abs foot-list">
  <li>Home</li><li>About Us</li><li>Services</li><li>Conditions We Treat</li><li>New Patients</li><li>Contact Us</li>
</ul>
<div class="abs foot-title" style="left:872px">FIND US</div>
<div class="abs find" style="top:3088px"><svg width="18" height="24" viewBox="0 0 18 24"><path d="M9 0a9 9 0 0 1 9 9c0 7-9 15-9 15S0 16 0 9a9 9 0 0 1 9-9z" fill="#2a9bd6"/><circle cx="9" cy="9" r="3.5" fill="#5c7d46"/></svg><span>Maplecrest Behavioral Healthcare<br>Lorem Ipsum is simply dummy<br>text printing and typesetting</span></div>
<div class="abs find" style="top:3172px"><svg width="20" height="20" viewBox="0 0 20 20"><path d="M4 1l4 4-2 3 6 6 3-2 4 4-3 3C8 19 1 12 1 4z" fill="#2a9bd6"/></svg><span>+1-555-014-2290</span></div>
<div class="abs find" style="top:3222px"><svg width="20" height="20" viewBox="0 0 20 20"><path d="M4 1l4 4-2 3 6 6 3-2 4 4-3 3C8 19 1 12 1 4z" fill="#2a9bd6"/></svg><span>+1-555-014-2291</span></div>
<div class="abs find" style="top:3264px"><svg width="22" height="18" viewBox="0 0 22 18"><rect width="22" height="18" rx="2" fill="#2a9bd6"/><path d="M1 2l10 8 10-8" stroke="#5c7d46" stroke-width="2" fill="none"/></svg><span>hello@maplecrestcare.example</span></div>
<div class="abs social" style="left:876px"></div>
<div class="abs social" style="left:934px"></div>
<div class="abs social" style="left:991px"></div>
<div class="abs copy"><b>&copy; MAPLECREST BEHAVIORAL HEALTHCARE</b>- 2017, All Rights Reserved</div>

</body>
</html>
```